Quorvant Group Invitation

I need an invitation designed for both online and hard copy distribution. I'm uploading a poorly designed online invitation that includes our logo and the blue and black colors we want to use. The online invitation must have an area to embed video (see attached).

With regard to the hard copy invitation, we need it to be a 5x7 card. Where the embedded video is on the online version, we would like you to create an image that represents the terms "monetizing innovation". If you go to www.qvgroup.co, you can see what the company is using to express those words right now. There are no limitations to what you come up with for this visual.

Please note: The invitation both online and hardcopy must be designed so that all the information in the attached copy can be read. This includes: Logo, hosted by; When/date, where, two quotes, etc.

I've attached our logo files. You can use whichever logo file you want for your design.

Many thanks...looking forward to seeing all your great designs.
Updates

All - you do not need to follow our format for the invite as long as all the information we need is on it....Note:  we will need to be able to edit the information for other presentation.

EPS files of the logo have been added for those of you who have requested it.

Many thanks,

Marla

Reason: All, Apologies for the extension. The decision-makers have been travelling and have not had a chance to thoroughly review the designs. We really appreciate your patience. Many thanks, Marla

Target Market(s)

Investors and Media

Industry/Entity Type

It Company

Requirements
Must have
• Please use the blue and black colors as seen in the attached uploaded files.

```html
<!DOCTYPE html>
<html lang="en">
<head>
<meta charset="utf-8">
<title>Monetizing Innovation – Quorvant Group Invitation</title>
<link href="https://fonts.googleapis.com/css2?family=Noto+Sans:wght@400;700&display=swap" rel="stylesheet">
<style>
  :root {
    --navy-deep: #1b2a6b;
    --navy: #2c4aa0;
    --sky: #6e86d6;
    --orange: #f6a51c;
    --blue-text: #1f3f96;
    --ink: #111111;
    --white: #ffffff;
  }
  html, body {
    margin: 0;
    padding: 0;
    overflow: hidden;
    background: var(--white);
  }
  .invite {
    position: relative;
    width: 1200px;
    height: 928px;
    overflow: hidden;
    font-family: "Noto Sans", Verdana, sans-serif;
    background: var(--white);
  }
  .backdrop {
    position: absolute;
    inset: 0;
  }
  .title {
    position: absolute;
    top: 6px;
    left: 0;
    width: 1200px;
    margin: 0;
    text-align: center;
    font-size: 66px;
    font-weight: 700;
    color: var(--orange);
    letter-spacing: 1px;
    text-shadow: 2px 3px 2px rgba(10, 20, 60, 0.85);
  }
  .subtitle {
    position: absolute;
    top: 84px;
    left: 0;
    width: 1200px;
    margin: 0;
    text-align: center;
    font-size: 27px;
    font-weight: 700;
    color: var(--white);
    text-shadow: 2px 2px 2px rgba(10, 20, 60, 0.7);
  }
  .details {
    position: absolute;
    top: 232px;
    left: 20px;
    width: 400px;
    text-align: center;
    font-size: 25px;
    line-height: 32px;
  }
  .details p { margin: 0; }
  .accent { color: var(--orange); font-weight: 700; }
  .plain { color: var(--ink); font-weight: 400; }
  .when { margin-bottom: 34px !important; }
  .where { margin-bottom: 34px !important; }
  .video-block {
    position: absolute;
    top: 234px;
    left: 395px;
    width: 340px;
    text-align: center;
  }
  .video-headline {
    margin: 0 0 32px;
    font-size: 27px;
    font-weight: 700;
    color: var(--blue-text);
  }
  .video-frame {
    position: relative;
    width: 292px;
    height: 238px;
    margin: 0 auto;
    border: 2px solid #111;
    background: linear-gradient(160deg, #0b1530 0%, #2f5cb8 45%, #9ab8ee 60%, #1a2c66 100%);
  }
  .play-button {
    position: absolute;
    left: 8px;
    bottom: 8px;
  }
  .video-description {
    margin: 18px 0 0;
    font-size: 22.5px;
    line-height: 31px;
    color: var(--blue-text);
  }
  .hosts {
    position: absolute;
    top: 232px;
    right: 36px;
    width: 440px;
    text-align: right;
  }
  .hosts-title {
    margin: 0 0 34px;
    padding-right: 40px;
    font-size: 27px;
    font-weight: 700;
    color: var(--white);
    text-shadow: 2px 2px 2px rgba(10, 20, 60, 0.7);
  }
  .hosts ul {
    list-style: none;
    margin: 0;
    padding: 0;
    font-size: 24px;
    line-height: 38px;
    font-weight: 700;
    color: var(--orange);
    text-shadow: 1px 2px 2px rgba(10, 20, 60, 0.6);
  }
  .brand {
    position: absolute;
    left: 28px;
    top: 756px;
    display: flex;
    flex-direction: column;
    align-items: flex-start;
    gap: 10px;
  }
  .brand-mark {
    width: 64px;
    height: 64px;
    background: var(--navy);
  }
  .brand-name {
    font-size: 20px;
    font-weight: 700;
    color: var(--ink);
    line-height: 23px;
    width: 130px;
  }
  .website {
    position: absolute;
    left: 168px;
    top: 851px;
    margin: 0;
    font-size: 32px;
    line-height: 40px;
    font-weight: 700;
    color: var(--blue-text);
    white-space: nowrap;
  }
  .disclaimer {
    position: absolute;
    left: 466px;
    top: 864px;
    margin: 0;
    font-size: 18px;
    line-height: 24px;
    color: var(--ink);
    white-space: nowrap;
  }
</style>
</head>
<body>
<main class="invite">
  <svg class="backdrop" width="1200" height="928" viewBox="0 0 1200 928">
    <defs>
      <linearGradient id="skyline" x1="0" y1="0" x2="1" y2="1">
        <stop offset="0" stop-color="#243a8a"/>
        <stop offset="0.5" stop-color="#3a57b4"/>
        <stop offset="1" stop-color="#1b2a6b"/>
      </linearGradient>
    </defs>
    <rect role="img" aria-label="Illustration of a blue city skyline with tall towers" x="0" y="0" width="1200" height="928" fill="url(#skyline)"/>
    <path d="M0,192 C250,148 560,112 880,120 L880,560 Q1020,610 1200,566 L1200,928 L0,928 Z" fill="#ffffff"/>
    <path d="M0,192 C250,148 560,112 880,120" fill="none" stroke="#8ea3e4" stroke-width="4" opacity="0.6"/>
  </svg>

  <h1 class="title">Monetizing Innovation</h1>
  <p class="subtitle">A Special Presentation</p>

  <section class="details">
    <p class="accent">Wednesday, September 28th</p>
    <p class="accent">Check-In 3:00 pm</p>
    <p class="accent when">Presentation 3:30 - 4:30 pm</p>
    <p class="accent">Harbor Hall – Cedar Room</p>
    <p class="accent">1280 Lakeview Ave</p>
    <p class="accent where">Fairmont CA 90000</p>
    <p class="plain">Please RSVP by</p>
    <p class="accent">Monday, September 26th</p>
    <p class="plain">Clara Whitfield</p>
    <p class="accent">(555) 210-4870 x1003</p>
    <p class="accent">cwhitfield@qvgroup.co</p>
  </section>

  <section class="video-block">
    <h2 class="video-headline">Video Headline</h2>
    <div class="video-frame" role="img" aria-label="Embedded video still of a vehicle in motion">
      <svg class="play-button" width="24" height="24" viewBox="0 0 24 24" aria-hidden="true">
        <rect x="1" y="1" width="22" height="22" fill="#222" stroke="#ccc" stroke-width="2"/>
        <path d="M8,6 L18,12 L8,18 Z" fill="#ddd"/>
      </svg>
    </div>
    <p class="video-description">Description of Video and so on and so on and so on with just a little bit more here and even more if necessary</p>
  </section>

  <section class="hosts">
    <h2 class="hosts-title">Hosted By:</h2>
    <ul>
      <li>Ravi Okonkwo, CEO</li>
      <li>Glen Marsh, President</li>
      <li>Luis Ortega, CFO</li>
      <li>Neil Brandt, COO</li>
      <li>Owen Tate, CCO</li>
    </ul>
  </section>

  <div class="brand">
    <span class="brand-mark"></span>
    <span class="brand-name">Quorvant Group</span>
  </div>
  <p class="website">www.qvgroup.co</p>
  <p class="disclaimer">*Please note that you must be an accredited investor to attend the presentation</p>
</main>
</body>
</html>
```